Research and Development Technical Training for Process Engineering

We are creating a Portalis site that will contain links to several training materials. I will create and upload the content, just looking for graphics and a basic layout for a single homepage. The page should contain unique graphics for the following topics/categories: Methodology, Equipment Training, Design References, Safety & Environmental, and Technology. (See attached example. Layout example DOES NOT need to be followed, only an example).
Also, a graphic to be used for a Powerpoint template that is cohesive with the graphics previously mentioned. Space for a company logo required. Professional/business application. Company logo already exists, it is blue and red but these colors are not required to be used as a theme.
Industry/Entity Type
Training
Number of Pages Required
1 page
Colors
Designer to choose colors to be used in the design.
Look and feel

```html
<!DOCTYPE html>
<html lang="en">
<head>
<meta charset="utf-8">
<title>Meridian — Research &amp; Development Training</title>
<link href="https://fonts.googleapis.com/css2?family=Montserrat:wght@400;500;600;700&display=swap" rel="stylesheet">
<style>
:root{
  --navy:#061a3d;
  --navy-deep:#020c22;
  --navy-mid:#0b2f6b;
  --blue:#1b72d8;
  --blue-band:rgba(23,110,220,.92);
  --red:#c50b0b;
  --ink:#111;
  --muted:#555;
  --grey-bg:#ececec;
  --line:#cfcfcf;
  --white:#fff;
}
*{margin:0;padding:0;box-sizing:border-box}
html,body{width:1200px;height:2486px;overflow:hidden;background:var(--white)}
body{font-family:"Montserrat",Arial,sans-serif;color:var(--ink);position:relative}
.abs{position:absolute}

/* hero */
.hero{left:0;top:0;width:1200px;height:578px;
  background:
    radial-gradient(circle at 8% 78%,rgba(40,110,220,.55) 0%,rgba(40,110,220,0) 22%),
    radial-gradient(circle at 92% 18%,rgba(60,130,230,.45) 0%,rgba(60,130,230,0) 26%),
    radial-gradient(circle at 60% 55%,rgba(30,80,170,.5) 0%,rgba(30,80,170,0) 40%),
    radial-gradient(circle at 30% 20%,rgba(20,60,140,.5) 0%,rgba(20,60,140,0) 35%),
    linear-gradient(160deg,#031236 0%,var(--navy) 50%,#0a2a66 100%)}
.brand{font-weight:700;letter-spacing:6px;font-size:19px;color:var(--white)}
.nav{right:68px;top:50px;display:flex;gap:48px;list-style:none}
.nav li{color:var(--white);font-size:17px;font-weight:500}
.hero-title{left:0;width:1200px;top:248px;text-align:center;color:var(--white);font-size:43px;font-weight:500}
.btn{display:flex;align-items:center;justify-content:center;background:var(--red);color:var(--white);
  font-size:13px;font-weight:600;border-radius:21px;height:41px;width:222px;letter-spacing:.3px;text-decoration:none}
.dots{left:560px;top:510px;display:flex;gap:15px}
.dots span{width:8px;height:8px;border-radius:50%;background:var(--white)}
.dots span:first-child{background:var(--blue)}

/* intro */
.intro-title{left:96px;top:622px;font-size:30px;font-weight:600}
.intro-sub{left:96px;top:663px;font-size:12px;color:var(--muted)}
.intro-body{left:96px;top:697px;width:560px;font-size:12.5px;line-height:24px;color:#333}
.portal-mark{left:779px;top:655px;display:flex;align-items:center;gap:18px}
.portal-mark .sq{width:84px;height:84px;background:var(--blue)}
.portal-mark .name{font-size:40px;font-weight:500;color:var(--blue)}

/* topics */
.topics{left:0;top:810px;width:1200px;height:661px;background:var(--grey-bg)}
.card{overflow:hidden}
.card .photo{position:absolute;inset:0}
.card .band{position:absolute;left:0;right:0;bottom:0;height:63px;background:var(--blue-band);
  color:var(--white);font-size:24px;font-weight:500;display:flex;align-items:center;justify-content:center}
.card-method{left:68px;top:863px;width:336px;height:259px;
  background:
    radial-gradient(circle at 85% 20%,rgba(70,110,120,.35) 0%,rgba(70,110,120,0) 35%),
    radial-gradient(circle at 15% 85%,rgba(60,90,100,.3) 0%,rgba(60,90,100,0) 35%),
    radial-gradient(circle at 45% 45%,#1c2b33 0%,#070b0e 80%);
  color:var(--white);text-align:center}
.card-method h3{margin-top:50px;font-size:24px;font-weight:500}
.card-method p{margin:20px auto 0;width:240px;font-size:12px;line-height:16px;color:rgba(255,255,255,.35)}
.card-method .btn{width:130px;height:25px;font-size:12px;margin:14px auto 0;border-radius:13px}

.photo-lab{background:
  radial-gradient(ellipse at 72% 28%,rgba(40,50,70,.75) 0%,rgba(40,50,70,0) 22%),
  radial-gradient(ellipse at 45% 60%,rgba(240,244,246,.95) 0%,rgba(240,244,246,0) 30%),
  radial-gradient(ellipse at 80% 70%,rgba(40,90,190,.6) 0%,rgba(40,90,190,0) 25%),
  linear-gradient(120deg,#e4eef2 0%,#b9d0da 45%,#7f9fb0 100%)}
.photo-keys{background:
  radial-gradient(ellipse at 60% 45%,rgba(190,150,120,.85) 0%,rgba(190,150,120,0) 30%),
  radial-gradient(ellipse at 85% 80%,rgba(220,220,225,.8) 0%,rgba(220,220,225,0) 30%),
  radial-gradient(ellipse at 95% 10%,rgba(230,170,90,.7) 0%,rgba(230,170,90,0) 25%),
  linear-gradient(135deg,#1f2a3a 0%,#3d4450 50%,#8c8b8d 100%)}
.photo-sprout{background:
  radial-gradient(ellipse at 36% 45%,rgba(160,205,70,.95) 0%,rgba(160,205,70,0) 14%),
  radial-gradient(ellipse at 70% 30%,rgba(150,160,60,.6) 0%,rgba(150,160,60,0) 40%),
  linear-gradient(180deg,#3f4e18 0%,#7f8f2d 45%,#6a6a28 62%,#3a2814 78%,#24170b 100%)}
.photo-desk{background:
  radial-gradient(ellipse at 45% 40%,rgba(235,238,242,.95) 0%,rgba(235,238,242,0) 26%),
  radial-gradient(ellipse at 95% 5%,rgba(220,90,30,.85) 0%,rgba(220,90,30,0) 28%),
  radial-gradient(ellipse at 80% 50%,rgba(150,100,80,.7) 0%,rgba(150,100,80,0) 22%),
  radial-gradient(ellipse at 10% 30%,rgba(60,90,60,.7) 0%,rgba(60,90,60,0) 18%),
  linear-gradient(160deg,#3d3b39 0%,#a6a39e 55%,#d8d4cf 100%)}

/* news */
.news-title{left:68px;top:1516px;font-size:31px;font-weight:500}
.news-sub{left:68px;top:1557px;font-size:12px;color:var(--muted)}
.news-rule{left:393px;top:1548px;width:739px;height:2px;background:var(--line)}
.news-photo{width:245px;height:150px}
.photo-touch{background:
  radial-gradient(circle at 55% 45%,rgba(120,200,255,.8) 0%,rgba(120,200,255,0) 25%),
  radial-gradient(circle at 85% 30%,rgba(60,140,230,.6) 0%,rgba(60,140,230,0) 30%),
  linear-gradient(135deg,#07183a 0%,#134a92 55%,#0b2350 100%)}
.photo-globe{background:
  radial-gradient(circle at 58% 55%,rgba(140,190,240,.75) 0%,rgba(140,190,240,0) 28%),
  radial-gradient(circle at 20% 40%,rgba(40,60,100,.8) 0%,rgba(40,60,100,0) 30%),
  linear-gradient(135deg,#050f26 0%,#15376e 60%,#081a3a 100%)}
.photo-team{background:
  radial-gradient(ellipse at 30% 55%,rgba(120,80,60,.8) 0%,rgba(120,80,60,0) 25%),
  radial-gradient(ellipse at 80% 40%,rgba(70,90,120,.7) 0%,rgba(70,90,120,0) 25%),
  linear-gradient(135deg,#f0eeea 0%,#c9c2b8 45%,#6a5d52 100%)}
.photo-wood{background:
  radial-gradient(ellipse at 70% 45%,rgba(60,60,70,.8) 0%,rgba(60,60,70,0) 22%),
  radial-gradient(ellipse at 25% 70%,rgba(230,225,215,.8) 0%,rgba(230,225,215,0) 22%),
  linear-gradient(135deg,#5c3d22 0%,#a97c52 50%,#6b4a2c 100%)}
.date-tag{background:#c01212;color:var(--white);font-size:12px;font-weight:600;width:134px;height:25px;
  display:flex;align-items:center;justify-content:center}
.news-text{width:262px}
.news-text h4{font-size:16px;font-weight:500;line-height:20px}
.news-text p{margin-top:12px;font-size:12.5px;line-height:18px;color:#333}

/* cta */
.cta{left:0;top:2035px;width:1200px;height:384px;
  background:
    radial-gradient(ellipse at 80% 95%,rgba(70,160,255,.55) 0%,rgba(70,160,255,0) 30%),
    radial-gradient(ellipse at 20% 90%,rgba(50,130,230,.5) 0%,rgba(50,130,230,0) 28%),
    radial-gradient(ellipse at 50% 40%,rgba(20,70,150,.5) 0%,rgba(20,70,150,0) 45%),
    linear-gradient(180deg,var(--navy-deep) 0%,var(--navy) 55%,#0e4fa8 100%)}
.cta-title{left:0;width:1200px;top:2148px;text-align:center;color:var(--white);font-size:37px;line-height:43px;font-weight:500}

/* footer */
.footer .brand{left:78px;top:2443px;color:var(--ink);font-size:18px}
.copyright{right:68px;top:2448px;font-size:12px;color:#333}
</style>
</head>
<body>

<header class="abs hero" role="img" aria-label="Dark blue abstract network of connected points and lines"></header>
<div class="abs brand" style="left:68px;top:50px">MERIDIAN</div>
<ul class="abs nav">
  <li>Home</li><li>About Us</li><li>Services</li><li>News</li><li>Contact Us</li>
</ul>
<h1 class="abs hero-title">Research &amp; Development Training</h1>
<a class="abs btn" style="left:489px;top:317px">LEARN MORE</a>
<div class="abs dots"><span></span><span></span><span></span><span></span></div>

<section>
  <h2 class="abs intro-title">Portalis</h2>
  <p class="abs intro-sub">Neque porro quisquam est qui dolorem ipsum quia</p>
  <p class="abs intro-body">At vero eos et accusamus et iusto odio dignissimos ducimus qui blanditiis praesentium voluptatum deleniti atque corrupti quos dolores et quas molestias excepturi sint occaecati cupiditate non provident, similique sunt</p>
  <div class="abs portal-mark"><span class="sq"></span><span class="name">Portalis</span></div>
</section>

<section class="abs topics"></section>
<div class="abs card card-method" role="img" aria-label="Dark background with faint network lines">
  <h3>Methodology</h3>
  <p>At vero eos et accusamus et iusto odio dignissimos ducimus qui blanditiis praesentium voluptatum deleniti atque corrupti quos dolores et quas</p>
  <div class="btn">READ MORE</div>
</div>
<div class="abs card" style="left:431px;top:863px;width:336px;height:259px">
  <div class="photo photo-lab" role="img" aria-label="Scientist looking into a microscope in a lab"></div>
  <div class="band">Equipment</div>
</div>
<div class="abs card" style="left:795px;top:863px;width:337px;height:259px">
  <div class="photo photo-keys" role="img" aria-label="Hands typing on a laptop keyboard"></div>
  <div class="band">Design References</div>
</div>
<div class="abs card" style="left:68px;top:1152px;width:517px;height:258px">
  <div class="photo photo-sprout" role="img" aria-label="Young green sprout growing from soil"></div>
  <div class="band">Safety &amp; Environmental</div>
</div>
<div class="abs card" style="left:611px;top:1152px;width:519px;height:258px">
  <div class="photo photo-desk" role="img" aria-label="Person at a desk with laptop and smartphone"></div>
  <div class="band">Technology</div>
</div>

<section>
  <h2 class="abs news-title">Latest News</h2>
  <p class="abs news-sub">Neque porro quisquam est qui dolorem ipsum quia</p>
  <div class="abs news-rule"></div>

  <div class="abs news-photo photo-touch" style="left:68px;top:1625px" role="img" aria-label="Hand touching a glowing digital interface"></div>
  <div class="abs date-tag" style="left:76px;top:1617px">March 22nd 2018</div>
  <div class="abs news-text" style="left:341px;top:1642px"><h4>Neque porro quisquam est qui dolorem ipsum quia</h4><p>At vero eos et accusamus et iusto odio dignissimos ducimus qui blanditiis praesentium voluptatum deleniti atque corrupti quos dolores et</p></div>

  <div class="abs news-photo photo-globe" style="left:611px;top:1625px" role="img" aria-label="Business person with a glowing globe network"></div>
  <div class="abs date-tag" style="left:619px;top:1617px">March 22nd 2018</div>
  <div class="abs news-text" style="left:885px;top:1642px"><h4>Neque porro quisquam est qui dolorem ipsum quia</h4><p>At vero eos et accusamus et iusto odio dignissimos ducimus qui blanditiis praesentium voluptatum deleniti atque corrupti quos dolores et</p></div>

  <div class="abs news-photo photo-team" style="left:68px;top:1818px" role="img" aria-label="Team meeting around a table with laptops"></div>
  <div class="abs date-tag" style="left:76px;top:1810px">March 22nd 2018</div>
  <div class="abs news-text" style="left:341px;top:1830px"><h4>Neque porro quisquam est qui dolorem ipsum quia</h4><p>At vero eos et accusamus et iusto odio dignissimos ducimus qui blanditiis praesentium voluptatum deleniti atque corrupti quos dolores et</p></div>

  <div class="abs news-photo photo-wood" style="left:611px;top:1818px" role="img" aria-label="Wooden desk with laptop and notebooks"></div>
  <div class="abs date-tag" style="left:619px;top:1810px">March 22nd 2018</div>
  <div class="abs news-text" style="left:885px;top:1830px"><h4>Neque porro quisquam est qui dolorem ipsum quia</h4><p>At vero eos et accusamus et iusto odio dignissimos ducimus qui blanditiis praesentium voluptatum deleniti atque corrupti quos dolores et</p></div>
</section>

<section class="abs cta" role="img" aria-label="Deep blue background with glowing network of connected nodes">
  <a class="abs btn" style="left:489px;top:237px">CONTACT US</a>
</section>
<h2 class="abs cta-title">Research &amp; Development Technical Training<br>company for Process Engineering.</h2>

<footer class="footer">
  <div class="abs brand">MERIDIAN</div>
  <p class="abs copyright">© 2018 Company Name &nbsp;|&nbsp; All Rights Reserved</p>
</footer>

</body>
</html>
```